Stainless Steel Letter Box plate

I need to have a letter box plate front in stainless steel that I what to have designed.

I have attached the Design of the brick letter box that has already been made.

The dimensions of the brick are set and the hole for the letters is in a set location. ( Give or take small amount )

The stainless steel manufacturer has sent a draft of the front of the plate that I thought was a bit boring and plain ( Attached )

The Stainless plate is to go on the front of the Letter box and wrap around to the left side. Brick and render will be ( is to be ) shown on the top and bottom margins of the stainless steel plate

Remember it needs to be cut out of Stainless Steel so that the number 4 needs to have joins.

The Stainless will go on the Front of the letter box and wrap around the left hand side of the letter box.

Industry/Entity Type

Steel

Requirements
Must have
• Letter Drop needs to be in set location
• Number 4
• Marrow or Marrow Rd

```html
<!DOCTYPE html>
<html lang="en">
<head>
<meta charset="utf-8">
<title>Marrow Rd – Letter Box Plate Concepts</title>
<link rel="stylesheet" href="https://fonts.googleapis.com/css2?family=Archivo+Black&family=Poiret+One&family=Raleway:wght@200&family=Roboto:wght@900&family=Oswald:wght@500;700&family=Josefin+Sans:wght@400&family=Didact+Gothic&family=Archivo:wght@800&family=Quicksand:wght@500&family=Share+Tech+Mono&display=swap">
<style>
  :root {
    --page: #ffffff;
    --label: #b4b4b4;
    --ink: #222222;
    --ink-light: #d9d9d9;
    --steel-dark: #a8a8a8;
    --steel-mid: #d2d2d2;
    --steel-light: #f7f7f7;
    --highlight: #ffffff;
  }
  html, body {
    margin: 0;
    padding: 0;
    width: 1200px;
    height: 899px;
    overflow: hidden;
    background: var(--page);
  }
  .sheet {
    position: relative;
    width: 1200px;
    height: 899px;
  }
  .concept {
    position: absolute;
    left: var(--x);
    top: var(--y);
  }
  .concept-number {
    position: absolute;
    left: -52px;
    top: 10px;
    font-family: "Share Tech Mono", monospace;
    font-size: 17px;
    letter-spacing: 7px;
    color: var(--label);
  }
  .plate {
    position: relative;
    width: 425px;
    height: 118px;
    overflow: hidden;
    background:
      radial-gradient(ellipse 60% 120% at 62% 0%, rgba(255,255,255,0.55), rgba(255,255,255,0) 70%),
      linear-gradient(112deg,
        var(--steel-dark) 0%,
        var(--steel-mid) 22%,
        var(--steel-light) 42%,
        var(--steel-mid) 55%,
        var(--steel-light) 70%,
        var(--highlight) 78%,
        var(--steel-mid) 92%,
        var(--steel-dark) 100%);
  }
  .letter-slot {
    position: absolute;
    left: 88px;
    top: 25px;
    width: 110px;
    height: 18px;
    background: var(--ink);
    box-shadow: 1px 1px 0 var(--highlight);
  }
  .street-name {
    position: absolute;
    left: 88px;
    bottom: 16px;
    margin: 0;
    font-size: 26px;
    line-height: 1;
    white-space: nowrap;
    color: var(--ink);
    text-shadow: 1px 1px 0 var(--highlight), -1px -1px 0 rgba(0,0,0,0.25);
  }
  .house-number {
    position: absolute;
    right: 28px;
    top: 50%;
    transform: translateY(-50%);
    margin: 0;
    font-size: 100px;
    line-height: 1;
    color: var(--ink);
    text-shadow: 2px 2px 0 var(--highlight), -2px -1px 0 rgba(0,0,0,0.3);
  }
  .engraved .street-name,
  .engraved .house-number {
    color: var(--ink-light);
    text-shadow: 1px 1px 0 #555, -1px -1px 0 var(--highlight);
  }

  .style-block .street-name { font-family: "Archivo Black", sans-serif; font-size: 23px; }
  .style-block .house-number { font-family: "Archivo Black", sans-serif; font-size: 104px; }

  .style-deco .street-name { font-family: "Poiret One", sans-serif; letter-spacing: 1px; }
  .style-deco .house-number { font-family: "Poiret One", sans-serif; }

  .style-hairline .street-name { font-family: "Raleway", sans-serif; font-weight: 200; }
  .style-hairline .house-number { font-family: "Raleway", sans-serif; font-weight: 200; }

  .style-heavy .street-name { font-family: "Roboto", sans-serif; font-weight: 900; font-size: 25px; }
  .style-heavy .house-number { font-family: "Roboto", sans-serif; font-weight: 900; }

  .style-condensed .street-name { font-family: "Oswald", sans-serif; font-weight: 500; font-size: 28px; letter-spacing: 1px; }
  .style-condensed .house-number { font-family: "Oswald", sans-serif; font-weight: 500; font-size: 96px; }

  .style-open .street-name { font-family: "Josefin Sans", sans-serif; letter-spacing: 2px; }
  .style-open .house-number { font-family: "Josefin Sans", sans-serif; }

  .style-gothic .street-name { font-family: "Didact Gothic", sans-serif; }
  .style-gothic .house-number { font-family: "Didact Gothic", sans-serif; font-style: italic; font-size: 80px; }

  .style-spaced .street-name { font-family: "Archivo", sans-serif; font-weight: 800; font-size: 24px; letter-spacing: 2px; }
  .style-spaced .house-number { font-family: "Archivo", sans-serif; font-weight: 800; font-size: 96px; }

  .style-rounded .street-name { font-family: "Quicksand", sans-serif; font-weight: 500; letter-spacing: 2px; }
  .style-rounded .house-number { font-family: "Quicksand", sans-serif; font-weight: 500; font-style: italic; }

  .style-tall .street-name { font-family: "Oswald", sans-serif; font-weight: 700; font-size: 27px; letter-spacing: 2px; }
  .style-tall .house-number { font-family: "Oswald", sans-serif; font-weight: 700; font-size: 90px; }
</style>
</head>
<body>
<main class="sheet">

  <section class="concept style-block" style="--x:120px; --y:68px;">
    <span class="concept-number">11</span>
    <div class="plate"><div class="letter-slot"></div><p class="street-name">MARROW RD</p><p class="house-number">4</p></div>
  </section>

  <section class="concept style-deco engraved" style="--x:708px; --y:68px;">
    <span class="concept-number">12</span>
    <div class="plate"><div class="letter-slot"></div><p class="street-name">MARROW RD</p><p class="house-number">4</p></div>
  </section>

  <section class="concept style-hairline engraved" style="--x:120px; --y:230px;">
    <span class="concept-number">13</span>
    <div class="plate"><div class="letter-slot"></div><p class="street-name">MARROW RD</p><p class="house-number">4</p></div>
  </section>

  <section class="concept style-heavy" style="--x:708px; --y:232px;">
    <span class="concept-number">14</span>
    <div class="plate"><div class="letter-slot"></div><p class="street-name">MARROW RD</p><p class="house-number">4</p></div>
  </section>

  <section class="concept style-condensed" style="--x:120px; --y:392px;">
    <span class="concept-number">15</span>
    <div class="plate"><div class="letter-slot"></div><p class="street-name">MARROW RD</p><p class="house-number">4</p></div>
  </section>

  <section class="concept style-open" style="--x:708px; --y:392px;">
    <span class="concept-number">16</span>
    <div class="plate"><div class="letter-slot"></div><p class="street-name">MARROW RD</p><p class="house-number">4</p></div>
  </section>

  <section class="concept style-gothic" style="--x:120px; --y:554px;">
    <span class="concept-number">17</span>
    <div class="plate"><div class="letter-slot"></div><p class="street-name">MARROW RD</p><p class="house-number">4</p></div>
  </section>

  <section class="concept style-spaced" style="--x:708px; --y:554px;">
    <span class="concept-number">18</span>
    <div class="plate"><div class="letter-slot"></div><p class="street-name">MARROW RD</p><p class="house-number">4</p></div>
  </section>

  <section class="concept style-rounded" style="--x:120px; --y:714px;">
    <span class="concept-number">19</span>
    <div class="plate"><div class="letter-slot"></div><p class="street-name">MARROW RD</p><p class="house-number">4</p></div>
  </section>

  <section class="concept style-tall" style="--x:708px; --y:714px;">
    <span class="concept-number">20</span>
    <div class="plate"><div class="letter-slot"></div><p class="street-name">MARROW RD</p><p class="house-number">4</p></div>
  </section>

</main>
</body>
</html>
```